Business Card Design Project

I need a business card designed with these details on the front along with the logo attached on the front.

Address - 518/ 217 Wendlebury st Thornvale
Website - www.brackenhollowmasonry.com.au
Email - delwyn@brackenhollowmasonry.com.au
Fax - 1900 457 618
Mobile - 0471926038
Telephone - 1300517926
Licence number - 847263k

```html
<!DOCTYPE html>
<html lang="en">
<head>
<meta charset="utf-8">
<title>Bracken Hollow Masonry – Business Card</title>
<link rel="stylesheet" href="https://fonts.googleapis.com/css2?family=Roboto+Condensed:wght@400;500;700&display=swap">
<style>
  :root {
    --page-bg: #1b1b1b;
    --card-border: #d9b48c;
    --stone-dark: #3f1f10;
    --stone-mid: #6e3419;
    --stone-glow: #b35a27;
    --band: rgba(28, 12, 5, 0.62);
    --text: #f6ede2;
    --text-soft: #efe3d4;
    --mark-fill: #d2c2a8;
    --mark-edge: #a8977d;
  }
  * { box-sizing: border-box; margin: 0; padding: 0; }
  html, body {
    width: 1200px; height: 686px; overflow: hidden;
    background: var(--page-bg);
  }
  body {
    font-family: "Roboto Condensed", "Arial Narrow", sans-serif;
    color: var(--text);
    position: relative;
  }
  .card {
    position: absolute; left: 20px; top: 10px;
    width: 1160px; height: 666px;
    border: 1px solid var(--card-border);
    overflow: hidden;
  }
  .stone-texture {
    position: absolute; inset: 0;
    background:
      radial-gradient(ellipse 55% 60% at 62% 52%, var(--stone-glow) 0%, rgba(179,90,39,0) 70%),
      linear-gradient(180deg, var(--stone-mid) 0%, var(--stone-dark) 100%);
  }
  .band { position: absolute; left: 0; right: 0; background: var(--band); }
  .band-top { top: 56px; height: 186px; }
  .band-bottom { top: 580px; bottom: 0; }

  .brand {
    position: absolute; left: 68px; top: 90px;
    display: flex; align-items: center; gap: 20px;
  }
  .brand-mark {
    width: 116px; height: 116px;
    background: var(--mark-fill);
    border: 4px solid var(--mark-edge);
  }
  .brand-name {
    font-weight: 400; font-size: 44px; line-height: 1.05;
    letter-spacing: 1px; text-transform: uppercase;
    color: var(--text);
  }

  .person { position: absolute; right: 76px; top: 98px; text-align: right; }
  .person-name { font-weight: 700; font-size: 50px; line-height: 1; }
  .person-title { font-weight: 500; font-size: 27px; margin-top: 12px; color: var(--text-soft); }

  .contacts { position: absolute; list-style: none; }
  .contacts li {
    display: flex; align-items: center;
    height: 55px; font-weight: 500; font-size: 29px; color: var(--text-soft);
  }
  .contacts svg { width: 30px; height: 30px; fill: var(--text); flex: none; }
  .contacts-left { left: 66px; top: 385px; }
  .contacts-left svg { margin-right: 29px; }
  .contacts-right { right: 76px; top: 378px; }
  .contacts-right svg { margin-right: 24px; }

  .licence {
    position: absolute; left: 0; right: 0; top: 580px; bottom: 0;
    display: flex; align-items: center; justify-content: center;
    font-weight: 500; font-size: 29px; color: var(--text-soft);
  }
</style>
</head>
<body>
<main class="card">
  <div class="stone-texture" role="img" aria-label="Warm brown sandstone wall texture"></div>
  <div class="band band-top"></div>
  <div class="band band-bottom"></div>

  <div class="brand">
    <div class="brand-mark"></div>
    <div class="brand-name">Bracken Hollow<br>Masonry</div>
  </div>

  <div class="person">
    <div class="person-name">Delwyn Carraway</div>
    <div class="person-title">Managing Director</div>
  </div>

  <ul class="contacts contacts-left">
    <li>
      <svg viewBox="0 0 24 24" aria-hidden="true"><path d="M6.6 2.5l3 3.2-1.8 2.6c1.2 2.6 3.3 4.7 5.9 5.9l2.6-1.8 3.2 3-1.9 3.6C10.3 18.6 5.4 13.7 3 6.4z"/></svg>
      1300517926
    </li>
    <li>
      <svg viewBox="0 0 24 24" aria-hidden="true"><path d="M7 1.5h10a1.5 1.5 0 0 1 1.5 1.5v18a1.5 1.5 0 0 1-1.5 1.5H7A1.5 1.5 0 0 1 5.5 21V3A1.5 1.5 0 0 1 7 1.5zm.5 3v13h9v-13zm4.5 14.5a1.2 1.2 0 1 0 0 2.4 1.2 1.2 0 0 0 0-2.4z"/></svg>
      0471926038
    </li>
    <li>
      <svg viewBox="0 0 24 24" aria-hidden="true"><path d="M6 3h12v5H6zM3 9h18v8h-3v-3H6v3H3zm4 6h10v6H7z"/></svg>
      1900 457 618
    </li>
  </ul>

  <ul class="contacts contacts-right">
    <li>
      <svg viewBox="0 0 24 24" aria-hidden="true"><path d="M2 5h20v1.2l-10 7-10-7zm0 3.6l10 7 10-7V19H2z"/></svg>
      delwyn@brackenhollowmasonry.com.au
    </li>
    <li>
      <svg viewBox="0 0 24 24" aria-hidden="true" fill="none"><g fill="none" stroke="#f6ede2" stroke-width="1.6"><circle cx="12" cy="12" r="9.5"/><ellipse cx="12" cy="12" rx="4.3" ry="9.5"/><path d="M2.5 12h19M4 7h16M4 17h16"/></g></svg>
      www.brackenhollowmasonry.com.au
    </li>
    <li>
      <svg viewBox="0 0 24 24" aria-hidden="true"><path d="M12 1.5a7 7 0 0 0-7 7c0 5 7 14 7 14s7-9 7-14a7 7 0 0 0-7-7zm0 4.2a2.8 2.8 0 1 1 0 5.6 2.8 2.8 0 0 1 0-5.6z"/></svg>
      518/ 217 Wendlebury st Thornvale
    </li>
  </ul>

  <div class="licence">Licence number - 847263k</div>
</main>
</body>
</html>
```